Marlow Crest Holdings (Remodeling company) needs a logo and business card

We need a business card design for a new company. We "flip" upmarket houses (buy, remodel and sell) in the Austin, TX area. I'd like neutral colors (grey, white, gold black). I would like it to include a simple, clean logo. Our designs are modern and uncluttered and I would like that reflected in the business card design.

Target Market(s)

Young professionals, Families, Retirees. Our properties will sell for $750k+

Industry/Entity Type

Real Estate

Contact Information for Business Card

Marlow Crest Holdings
Nora Pellham
(555) 216 7042
Owner
Rory Tansil
(555) 638 1975
Realtor

Logo Text

Marlow Crest Holdings

Font styles to use
Serif
Script

Requirements
Must have
• Simple, classic design
Nice to have
• Clean lines, modern look
Should not have
• Too traditionally

```html
<!DOCTYPE html>
<html lang="en">
<head>
<meta charset="utf-8">
<title>Marlow Crest Holdings – Business Card</title>
<link rel="stylesheet" href="https://fonts.googleapis.com/css2?family=Open+Sans:wght@400;600;700&display=swap">
<style>
  :root {
    --page-bg: #2b2d31;
    --card-black: #050505;
    --gold: #f0b40c;
    --gold-deep: #c98f06;
    --silver: #b9bbbe;
    --white: #ffffff;
    --card-w: 560px;
    --card-h: 320px;
  }
  * { box-sizing: border-box; margin: 0; padding: 0; }
  html, body {
    width: 1200px;
    height: 864px;
    overflow: hidden;
    background: var(--page-bg);
    font-family: "Open Sans", Arial, sans-serif;
  }
  .card-sheet {
    position: relative;
    width: 1200px;
    height: 864px;
    display: flex;
    flex-direction: column;
    align-items: center;
    justify-content: center;
    gap: 48px;
  }
  .card {
    position: relative;
    width: var(--card-w);
    height: var(--card-h);
    background: var(--card-black);
    overflow: hidden;
    box-shadow: 0 10px 24px rgba(0,0,0,0.45);
  }
  .card__wave {
    position: absolute;
    inset: 0;
    width: 100%;
    height: 100%;
  }
  .brand-name {
    position: absolute;
    font-weight: 600;
    letter-spacing: 0.06em;
    text-transform: uppercase;
    white-space: nowrap;
  }
  .card--front .brand-name {
    right: 40px;
    bottom: 40px;
    font-size: 24px;
    color: var(--white);
  }
  .card--back .brand-name {
    left: 36px;
    top: 96px;
    font-size: 22px;
    color: var(--gold);
  }
  .contact {
    position: absolute;
    right: 40px;
    text-align: right;
    color: var(--white);
  }
  .contact__name {
    font-weight: 700;
    font-size: 19px;
    line-height: 1.2;
  }
  .contact__role {
    font-size: 14px;
    line-height: 1.5;
  }
  .contact__phone {
    font-size: 14px;
    line-height: 1.5;
    display: flex;
    align-items: center;
    justify-content: flex-end;
    gap: 6px;
  }
  .contact__icon { width: 14px; height: 12px; }
  .contact--realtor { top: 28px; }
  .contact--realtor .contact__name { color: var(--gold); }
  .contact--realtor .contact__icon { fill: var(--gold); }
  .contact--owner { bottom: 28px; }
  .contact--owner .contact__icon { fill: var(--white); }
</style>
</head>
<body>
<main class="card-sheet">

  <section class="card card--front" aria-label="Business card front">
    <svg class="card__wave" viewBox="0 0 560 320" preserveAspectRatio="none" aria-hidden="true">
      <defs>
        <linearGradient id="goldBandFront" x1="0" y1="0" x2="0" y2="1">
          <stop offset="0" stop-color="#f4bd12"/>
          <stop offset="1" stop-color="#c98f06"/>
        </linearGradient>
      </defs>
      <path d="M0,200 C110,168 240,170 330,188 S480,200 560,176 L560,320 L0,320 Z" fill="var(--silver)"/>
      <path d="M0,208 C110,176 240,178 330,196 S480,208 560,184 L560,320 L0,320 Z" fill="url(#goldBandFront)"/>
    </svg>
    <p class="brand-name">Marlow Crest Holdings</p>
  </section>

  <section class="card card--back" aria-label="Business card back">
    <svg class="card__wave" viewBox="0 0 560 320" preserveAspectRatio="none" aria-hidden="true">
      <defs>
        <linearGradient id="goldBandBack" x1="0" y1="0" x2="0" y2="1">
          <stop offset="0" stop-color="#f4bd12"/>
          <stop offset="1" stop-color="#c98f06"/>
        </linearGradient>
      </defs>
      <path d="M0,180 C80,208 200,200 300,190 S470,186 560,212 L560,320 L0,320 Z" fill="var(--silver)"/>
      <path d="M0,188 C80,216 200,208 300,198 S470,194 560,220 L560,320 L0,320 Z" fill="url(#goldBandBack)"/>
    </svg>

    <p class="brand-name">Marlow Crest Holdings</p>

    <div class="contact contact--realtor">
      <p class="contact__name">Rory Tansil</p>
      <p class="contact__role">Realtor</p>
      <p class="contact__phone">(555) 638 1975
        <svg class="contact__icon" viewBox="0 0 14 12" aria-hidden="true"><path d="M1,4 C1,1 13,1 13,4 L13,5 L10,5 L10,3.5 L4,3.5 L4,5 L1,5 Z M3,6 L11,6 L12.5,11 L1.5,11 Z"/></svg>
      </p>
    </div>

    <div class="contact contact--owner">
      <p class="contact__name">Nora Pellham</p>
      <p class="contact__role">Owner</p>
      <p class="contact__phone">(555) 216 7042
        <svg class="contact__icon" viewBox="0 0 14 12" aria-hidden="true"><path d="M1,4 C1,1 13,1 13,4 L13,5 L10,5 L10,3.5 L4,3.5 L4,5 L1,5 Z M3,6 L11,6 L12.5,11 L1.5,11 Z"/></svg>
      </p>
    </div>
  </section>

</main>
</body>
</html>
```